New Packaging Design Project

Wine packaging redesign. Retail partner requested a redesign of a private label wine. The old label is attached. Our partner liked the Copper Wren Hollow label and wanted something similar. There will be a logo added to the top of the label

Went on vacation/holiday

```html
<!DOCTYPE html>
<html lang="en">
<head>
<meta charset="utf-8">
<title>Alder Basin Red Blend Label</title>
<link rel="stylesheet" href="https://fonts.googleapis.com/css2?family=Cinzel:wght@400;500&family=Raleway:wght@400;500&family=EB+Garamond:wght@400&display=swap">
<style>
  :root {
    --page: #ffffff;
    --label: #4a4846;
    --gold: #c8a86a;
    --ivory: #ebe6de;
    --muted: #a9a298;
    --land-top: #5a524a;
    --land-mid: #7a6c5c;
    --land-low: #b8ac97;
  }
  html, body {
    margin: 0;
    padding: 0;
    width: 1200px;
    height: 2501px;
    overflow: hidden;
    background: var(--page);
  }
  .canvas {
    position: relative;
    width: 1200px;
    height: 2501px;
  }
  .label {
    position: absolute;
    left: 100px;
    top: 424px;
    width: 1000px;
    height: 1652px;
    background: var(--label);
    overflow: hidden;
    text-align: center;
  }
  .label__name {
    position: absolute;
    top: 300px;
    left: 0;
    right: 0;
    margin: 0;
    font-family: "Cinzel", serif;
    font-weight: 500;
    font-size: 100px;
    letter-spacing: 2px;
    color: var(--gold);
  }
  .label__style {
    position: absolute;
    top: 530px;
    left: 0;
    right: 0;
    margin: 0;
    font-family: "Raleway", sans-serif;
    font-weight: 500;
    font-size: 50px;
    letter-spacing: 1px;
    color: var(--ivory);
  }
  .label__varietals {
    position: absolute;
    top: 615px;
    left: 0;
    right: 0;
    margin: 0;
    font-family: "Raleway", sans-serif;
    font-size: 24px;
    line-height: 34px;
    letter-spacing: 0.5px;
    color: var(--muted);
  }
  .label__vintage {
    position: absolute;
    top: 698px;
    left: 0;
    right: 0;
    margin: 0;
    font-family: "EB Garamond", serif;
    font-size: 38px;
    color: var(--ivory);
  }
  .label__landscape {
    position: absolute;
    left: 0;
    top: 830px;
    width: 1000px;
    height: 822px;
  }
</style>
</head>
<body>
  <main class="canvas">
    <section class="label">
      <h1 class="label__name">Alder Basin</h1>
      <p class="label__style">RED BLEND</p>
      <p class="label__varietals">MERLOT | CABERNET SAUVIGNON<br>CABERNET FRANC | PETIT VERDOT | MALBEC</p>
      <p class="label__vintage">2020</p>
      <svg class="label__landscape" viewBox="0 0 1000 822" role="img" aria-label="Gold line illustration of a mountain ridge above rolling vineyard rows and layered hills">
        <defs>
          <linearGradient id="landscape-tone" x1="0" y1="0" x2="0" y2="1">
            <stop offset="0" stop-color="var(--label)"/>
            <stop offset="0.2" stop-color="var(--land-top)"/>
            <stop offset="0.65" stop-color="var(--land-mid)"/>
            <stop offset="1" stop-color="var(--land-low)"/>
          </linearGradient>
        </defs>
        <rect width="1000" height="822" fill="url(#landscape-tone)"/>
      </svg>
    </section>
  </main>
</body>
</html>
```